Powerpoint Template refresh and colors

I am doing consulting for a company that makes ingredients from plants for the pharma industry.

They have a small powerpoint template already (enclosed) but I need 4 or 5 more slides theme related to be presenting my conclusions. Those slides should have non-obstructive images of plants, particularly plants that the company uses (list enclosed).
You can use the images enclosed but even better if you can find some different and good pictures, if they are stock photos and I like the design I will pay for the material separately (just include for sample a photo with the frameloft watermark, no problem).

I also need a palette of colors to go with that template.
That palette would include 4 sets of 4 colors that I could use to make charts and graphs without disrupting the aesthetics of the presentation. I will also use those colors for the text of my presentation.

Green colors, grey, purple (thistle), some yellow go well with the theme of the company.

Thank you!

Font styles to use
Sans Serif

Colors
9ccb3b

Requirements
Must have
• Four or five slides that will hold text or text and charts.
• Each slide is to have a different picture of a plant in an non-obtrusive way.
• For instance:
• - a light background that does not interfere with text (like the palm shown)
• - or pictures of the plants at top/bottom of slides.
• My slide need space for text and charts, I do not like crowded slides.
• I will also need you to provide with the RGB definition of 4 sets of 4 colors.
• All colors in one set should match and will be used to present charts. For example the sales of 4 main plants in tones of green/yellow/brown/purple, see pictures attached.
• I need 4 sets of colors, the main colors are green/yellow/brown as shown in the enclosed pictures. The different sets do not have to match between each other.
Nice to have
• Some nice effects so that it does not look "flat".
Should not have
• aggressive design. I am looking for something smooth that flows ... at the end we make medicines out plants.

```html
<!DOCTYPE html>
<html lang="en">
<head>
<meta charset="utf-8">
<title>Simply Effective Presentation – Slide Overview</title>
<link href="https://fonts.googleapis.com/css2?family=Roboto:wght@300;400;500;700&display=swap" rel="stylesheet">
<style>
  :root{
    --canvas:#c9c5e3;
    --purple:#7a3ca6;
    --orange:#e8791e;
    --green:#9ccb3b;
    --green-light:#8fd14f;
    --yellow:#f3ec12;
    --brown:#8a4a12;
    --teal:#3e8a6e;
    --ink:#5a5a5a;
    --muted:#9a9a9a;
  }
  *{margin:0;padding:0;box-sizing:border-box}
  html,body{width:1200px;height:1010px;overflow:hidden;background:var(--canvas)}
  .overview{position:relative;width:1200px;height:1010px;font-family:"Roboto",sans-serif}
  .slide{position:absolute;width:240px;height:150px;overflow:hidden;box-shadow:0 1px 3px rgba(80,60,120,.15)}
  .slide text{font-family:"Roboto",sans-serif}
  .title{font-size:9px;fill:var(--purple);font-weight:300}
  .heading{font-size:6px;fill:var(--orange);font-weight:500}
  .body{font-size:4px;fill:var(--muted)}
  .label{font-size:3.6px;fill:var(--orange);font-weight:500}
  .day{font-size:3.6px;fill:var(--muted)}
  .tl-year{font-size:6px;fill:#b8c0bc}
  .bar-text{font-size:3.4px;fill:#fff}
  .legend{font-size:3.8px;fill:var(--ink)}
  .year{font-size:5px;fill:var(--ink);font-weight:500}
  .defs{position:absolute;width:0;height:0}
</style>
</head>
<body>
<svg class="defs" aria-hidden="true">
  <defs>
    <linearGradient id="slideBg" x1="0" y1="0" x2="0" y2="1">
      <stop offset="0" stop-color="#fbfdf3"/><stop offset=".78" stop-color="#e1efc7"/><stop offset="1" stop-color="#f5faec"/>
    </linearGradient>
    <linearGradient id="phMeadow" x1="0" y1="0" x2="1" y2="1"><stop offset="0" stop-color="#6f9a2a"/><stop offset=".5" stop-color="#b9d98a"/><stop offset="1" stop-color="#7fa83a"/></linearGradient>
    <radialGradient id="phDark"><stop offset="0" stop-color="#4a5a3a"/><stop offset="1" stop-color="#141a12"/></radialGradient>
    <radialGradient id="phThistle" cx=".35" cy=".4"><stop offset="0" stop-color="#c8306e"/><stop offset=".6" stop-color="#8a2a55"/><stop offset="1" stop-color="#4a6a2a"/></radialGradient>
    <radialGradient id="phSeed"><stop offset="0" stop-color="#a88a52"/><stop offset="1" stop-color="#6a5230"/></radialGradient>
    <radialGradient id="phPansy"><stop offset="0" stop-color="#f2e6a0"/><stop offset=".45" stop-color="#8a6ac0"/><stop offset="1" stop-color="#e4eede"/></radialGradient>
    <radialGradient id="phCone" cx=".4" cy=".35"><stop offset="0" stop-color="#d8609a"/><stop offset=".6" stop-color="#a04a70"/><stop offset="1" stop-color="#3a5a2a"/></radialGradient>
    <radialGradient id="phRoot"><stop offset="0" stop-color="#8a6a4a"/><stop offset="1" stop-color="#4a3422"/></radialGradient>
    <radialGradient id="phGold" cx=".4" cy=".4"><stop offset="0" stop-color="#e8c020"/><stop offset=".6" stop-color="#a89a20"/><stop offset="1" stop-color="#3a4a1a"/></radialGradient>
    <linearGradient id="phLavender" x1="0" y1="0" x2="1" y2="0"><stop offset="0" stop-color="#8a6ab8"/><stop offset=".5" stop-color="#b898d8"/><stop offset="1" stop-color="#6a8a4a"/></linearGradient>
    <linearGradient id="phHarbour" x1="0" y1="0" x2="0" y2="1"><stop offset="0" stop-color="#9ac0d8"/><stop offset="1" stop-color="#2a5a7a"/></linearGradient>
    <linearGradient id="phBlossom" x1="0" y1="0" x2="1" y2="1"><stop offset="0" stop-color="#e8a0b8"/><stop offset="1" stop-color="#6a8a4a"/></linearGradient>
    <clipPath id="slideClip"><rect width="300" height="187"/></clipPath>

    <g id="tab">
      <rect width="15" height="24" fill="#7a3ca6"/>
      <path d="M3 14h9M3 16.5h9M3 19h9" stroke="#fff" stroke-width=".6"/>
    </g>
    <g id="bodyBlock">
      <text class="body" y="0">Gentle plant extracts prepared with care for</text>
      <text class="body" y="5.5">pharma partners across the region. Each</text>
      <text class="body" y="11">ingredient is tested, traced and refined</text>
      <text class="body" y="16.5">for purity. Clear results, steady supply.</text>
    </g>
    <g id="desc">
      <rect x="-3" y="-4" width="1" height="16" fill="#e8791e"/>
      <text class="label" y="0">Description</text>
      <text class="body" y="5">Root extract yield grew steadily this year</text>
      <text class="body" y="10">across all main growing regions.</text>
    </g>
    <g id="legendList">
      <rect y="-3.5" width="1.2" height="4.5" fill="#7a3ca6"/><text class="legend" x="4" y="0">description area</text>
      <rect y="5" width="1.2" height="4.5" fill="#f3ec12"/><text class="legend" x="4" y="8.5">description location</text>
      <rect y="13.5" width="1.2" height="4.5" fill="#8fd14f"/><text class="legend" x="4" y="17">description space</text>
      <rect y="22" width="1.2" height="4.5" fill="#e8791e"/><text class="legend" x="4" y="25.5">description land</text>
    </g>
    <g id="pie">
      <path d="M0 0L0-50A50 50 0 0 1 29.4-40.5Z" fill="#e8791e"/>
      <path d="M0 0L29.4-40.5A50 50 0 1 1-47.6 15.5Z" fill="#8fd14f"/>
      <path d="M0 0L-47.6 15.5A50 50 0 0 1-29.4-40.5Z" fill="#f3ec12"/>
      <path d="M0 0L-29.4-40.5A50 50 0 0 1 0-50Z" fill="#7a3ca6"/>
      <text x="25" y="2" font-size="5" fill="#fff">60%</text>
      <text x="-21" y="-22" font-size="4" fill="#fff">10%</text>
      <text x="-3" y="-38" font-size="4" fill="#fff">10%</text>
      <text x="-36" y="6" font-size="4" fill="#fff">20%</text>
    </g>
    <g id="ring">
      <circle r="40" fill="none" stroke="#7a3ca6" stroke-width="13" stroke-dasharray="58 193.3" transform="rotate(-85)"/>
      <circle r="40" fill="none" stroke="#f3ec12" stroke-width="13" stroke-dasharray="58 193.3" transform="rotate(5)"/>
      <circle r="40" fill="none" stroke="#3e8a6e" stroke-width="13" stroke-dasharray="58 193.3" transform="rotate(95)"/>
      <circle r="40" fill="none" stroke="#e8791e" stroke-width="13" stroke-dasharray="58 193.3" transform="rotate(185)"/>
      <text text-anchor="middle" y="2" font-size="5" fill="#444">DESCRIPTION</text>
    </g>
  </defs>
</svg>

<main class="overview">

  <!-- Title -->
  <svg class="slide" style="left:48px;top:74px" viewBox="0 0 300 187">
    <rect width="300" height="187" fill="url(#slideBg)"/>
    <rect width="300" height="45" fill="url(#phMeadow)" role="img" aria-label="Photo of white star flowers in green grass"/>
    <rect width="14" height="45" fill="var(--purple)"/>
    <text x="27" y="76" font-size="20" font-weight="500" fill="var(--purple)">Simply Effective</text>
    <text x="27" y="103" font-size="20" font-weight="500" fill="var(--purple)">Presentation</text>
    <text x="27" y="135" font-size="8.5" fill="#555">The Ultimate Guide for Next Year</text>
    <text x="27" y="147" font-size="8.5" fill="#555">Marketing</text>
    <text x="27" y="171" font-size="4.5" fill="#444"><tspan font-weight="700">Lena Marovic</tspan>/ Feb 29, 2016</text>
  </svg>

  <!-- What we will do -->
  <svg class="slide" style="left:318px;top:74px" viewBox="0 0 300 187">
    <rect width="300" height="187" fill="url(#slideBg)"/>
    <g clip-path="url(#slideClip)">
      <circle cx="255" cy="90" r="100" fill="url(#phDark)" role="img" aria-label="Photo of white flower spike on a dark background"/>
    </g>
    <circle cx="208" cy="145" r="38" fill="url(#phSeed)" stroke="#fff" stroke-width="2" role="img" aria-label="Photo of dried roots"/>
    <use href="#tab"/>
    <text class="title" x="19" y="25">What we will do</text>
    <text class="heading" x="30" y="52">Super Plan 01</text>
    <use href="#bodyBlock" x="30" y="63"/>
    <text class="heading" x="30" y="113">Super Plan 02</text>
    <use href="#bodyBlock" x="30" y="124"/>
  </svg>

  <!-- Secret plan A/B -->
  <svg class="slide" style="left:628px;top:74px" viewBox="0 0 300 187">
    <rect width="300" height="187" fill="url(#slideBg)"/>
    <g clip-path="url(#slideClip)">
      <circle cx="20" cy="80" r="110" fill="url(#phThistle)" role="img" aria-label="Photo of a purple thistle flower"/>
    </g>
    <circle cx="88" cy="143" r="38" fill="url(#phSeed)" stroke="#fff" stroke-width="2" role="img" aria-label="Photo of thistle seeds"/>
    <use href="#tab" x="285"/>
    <text class="title" x="277" y="16" text-anchor="end">What is our secret plan?</text>
    <text class="heading" x="147" y="83">Super Plan A</text>
    <text class="body" x="138" y="94">Gentle plant extracts for pharma</text>
    <text class="body" x="138" y="99.5">partners, tested and refined.</text>
    <text class="heading" x="234" y="83">Super Plan B</text>
    <text class="body" x="219" y="94">Clear results and steady supply</text>
    <text class="body" x="219" y="99.5">from trusted growing regions.</text>
  </svg>

  <!-- Secret plan pansy -->
  <svg class="slide" style="left:924px;top:74px" viewBox="0 0 300 187">
    <rect width="300" height="187" fill="url(#slideBg)"/>
    <ellipse cx="75" cy="95" rx="72" ry="50" fill="url(#phPansy)" role="img" aria-label="Photo of a purple and white pansy"/>
    <use href="#tab"/>
    <text class="title" x="19" y="25">What is our secret plan?</text>
    <text class="heading" x="183" y="54">Super Plan 01</text>
    <use href="#bodyBlock" x="183" y="65"/>
    <use href="#bodyBlock" x="183" y="100"/>
  </svg>

  <!-- Secret plan echinacea -->
  <svg class="slide" style="left:48px;top:260px" viewBox="0 0 300 187">
    <rect width="300" height="187" fill="url(#slideBg)"/>
    <g clip-path="url(#slideClip)">
      <circle cx="265" cy="80" r="105" fill="url(#phCone)" role="img" aria-label="Photo of pink coneflowers"/>
    </g>
    <circle cx="205" cy="150" r="38" fill="url(#phRoot)" stroke="#fff" stroke-width="2" role="img" aria-label="Photo of dried coneflower roots"/>
    <use href="#tab"/>
    <text class="title" x="19" y="25">What is our secret plan?</text>
    <text class="heading" x="22" y="54">Super Plan 01</text>
    <use href="#bodyBlock" x="22" y="65"/>
    <use href="#bodyBlock" x="22" y="100"/>
  </svg>

  <!-- Gantt 1 -->
  <svg class="slide" style="left:318px;top:260px" viewBox="0 0 300 187">
    <rect width="300" height="187" fill="url(#slideBg)"/>
    <use href="#tab"/>
    <text class="title" x="19" y="25">Gantt Chart</text>
    <g class="gantt">
      <rect x="15" y="42" width="270" height="104" fill="#f6f8f2"/>
      <circle cx="48" cy="53" r="3" fill="none" stroke="var(--purple)" stroke-width=".7"/>
      <g text-anchor="middle">
        <text class="day" x="85" y="54">Mon</text><text class="day" x="116" y="54">Tue</text><text class="day" x="147" y="54">Wed</text><text class="day" x="178" y="54">Thu</text><text class="day" x="209" y="54">Fri</text><text class="day" x="240" y="54">Sat</text><text class="day" x="271" y="54">Sun</text>
      </g>
      <rect x="15" y="62" width="270" height="10.5" fill="#e8ece4"/><rect x="15" y="83" width="270" height="10.5" fill="#e8ece4"/><rect x="15" y="104" width="270" height="10.5" fill="#e8ece4"/><rect x="15" y="125" width="270" height="10.5" fill="#e8ece4"/>
      <g text-anchor="end">
        <text class="label" x="66" y="74">Task description here</text>
        <text class="label" x="66" y="94">Activity description</text>
        <text class="label" x="66" y="115">Replace with your text</text>
        <text class="label" x="66" y="136">Your text here</text>
      </g>
      <rect x="69" y="70" width="186" height="7" fill="var(--purple)"/><text class="bar-text" x="162" y="74.8" text-anchor="middle">example text</text>
      <rect x="100" y="91" width="62" height="7" fill="var(--yellow)"/><text class="bar-text" x="131" y="95.8" text-anchor="middle">example text</text>
      <rect x="100" y="112" width="124" height="7" fill="var(--orange)"/><text class="bar-text" x="162" y="116.8" text-anchor="middle">example text</text>
      <rect x="69" y="133" width="62" height="7" fill="var(--green-light)"/><text class="bar-text" x="100" y="137.8" text-anchor="middle">example text</text>
    </g>
  </svg>

  <!-- Gantt 2 -->
  <svg class="slide" style="left:628px;top:260px" viewBox="0 0 300 187">
    <rect width="300" height="187" fill="url(#slideBg)"/>
    <use href="#tab"/>
    <text class="title" x="19" y="25">Gantt Chart</text>
    <g class="gantt">
      <rect x="15" y="38" width="270" height="122" fill="#f6f8f2"/>
      <circle cx="50" cy="47" r="3" fill="none" stroke="var(--purple)" stroke-width=".7"/>
      <g text-anchor="middle">
        <text class="day" x="84" y="48">Mon</text><text class="day" x="115" y="48">Tue</text><text class="day" x="146" y="48">Wed</text><text class="day" x="177" y="48">Thu</text><text class="day" x="208" y="48">Fri</text><text class="day" x="239" y="48">Sat</text><text class="day" x="270" y="48">Sun</text>
      </g>
      <rect x="15" y="66" width="270" height="13.5" fill="#e8ece4"/><rect x="15" y="93" width="270" height="13.5" fill="#e8ece4"/><rect x="15" y="120" width="270" height="13.5" fill="#e8ece4"/><rect x="15" y="147" width="270" height="13" fill="#e8ece4"/>
      <g text-anchor="end">
        <text class="label" x="66" y="61">Task description</text>
        <text class="label" x="66" y="74">Activity description</text>
        <text class="label" x="66" y="88">Replace with yours</text>
        <text class="label" x="66" y="101">Your text here</text>
        <text class="label" x="66" y="115">Description here</text>
        <text class="label" x="66" y="128">Activity description</text>
        <text class="label" x="66" y="142">Replace text</text>
        <text class="label" x="66" y="155">Your text here</text>
      </g>
      <rect x="99" y="55" width="155" height="8" fill="var(--orange)"/><text class="bar-text" x="176" y="60.2" text-anchor="middle">example text</text>
      <rect x="69" y="69" width="62" height="8" fill="var(--purple)"/><text class="bar-text" x="100" y="74.2" text-anchor="middle">example text</text>
      <rect x="131" y="82" width="123" height="8" fill="var(--yellow)"/><text class="bar-text" x="192" y="87.2" text-anchor="middle">example text</text>
      <rect x="193" y="96" width="61" height="8" fill="var(--green-light)"/><text class="bar-text" x="223" y="101.2" text-anchor="middle">example text</text>
      <rect x="69" y="109" width="62" height="8" fill="var(--orange)"/><text class="bar-text" x="100" y="114.2" text-anchor="middle">example text</text>
      <rect x="162" y="123" width="123" height="8" fill="var(--yellow)"/><text class="bar-text" x="223" y="128.2" text-anchor="middle">example text</text>
      <rect x="131" y="150" width="62" height="8" fill="var(--purple)"/><text class="bar-text" x="162" y="155.2" text-anchor="middle">example text</text>
    </g>
  </svg>

  <!-- Pie 1 -->
  <svg class="slide" style="left:924px;top:260px" viewBox="0 0 300 187">
    <rect width="300" height="187" fill="url(#slideBg)"/>
    <use href="#tab"/>
    <text class="title" x="19" y="25">Pie Chart</text>
    <use href="#pie" x="82" y="92"/>
    <use href="#desc" x="172" y="42"/>
    <use href="#desc" x="172" y="71"/>
    <use href="#desc" x="172" y="100"/>
    <use href="#desc" x="172" y="129"/>
  </svg>

  <!-- Pie 2 -->
  <svg class="slide" style="left:48px;top:448px" viewBox="0 0 300 187">
    <rect width="300" height="187" fill="url(#slideBg)"/>
    <use href="#tab"/>
    <text class="title" x="19" y="25">Pie Chart</text>
    <text class="heading" x="22" y="48">Super Plan 01</text>
    <use href="#bodyBlock" x="22" y="59"/>
    <use href="#bodyBlock" x="22" y="81"/>
    <use href="#legendList" x="22" y="123"/>
    <g transform="translate(228 90) scale(.92)"><use href="#pie"/></g>
  </svg>

  <!-- Cycle 1 -->
  <svg class="slide" style="left:318px;top:448px" viewBox="0 0 300 187">
    <rect width="300" height="187" fill="url(#slideBg)"/>
    <use href="#tab"/>
    <text class="title" x="19" y="25">Cycle Diagram</text>
    <use href="#ring" x="84" y="94"/>
    <g font-size="4" fill="#fff" text-anchor="middle"><text x="88" y="54">A</text><text x="124" y="96">B</text><text x="76" y="140">C</text><text x="42" y="92">D</text></g>
    <use href="#desc" x="172" y="42"/>
    <use href="#desc" x="172" y="71"/>
    <use href="#desc" x="172" y="100"/>
    <use href="#desc" x="172" y="129"/>
  </svg>

  <!-- Cycle 2 -->
  <svg class="slide" style="left:628px;top:448px" viewBox="0 0 300 187">
    <rect width="300" height="187" fill="url(#slideBg)"/>
    <use href="#tab"/>
    <text class="title" x="19" y="25">Cycle Diagram</text>
    <g transform="translate(150 94) rotate(-90)">
      <circle r="40" fill="none" stroke="var(--green-light)" stroke-width="13" stroke-dasharray="58 193.3" transform="rotate(5)"/>
      <circle r="40" fill="none" stroke="var(--purple)" stroke-width="13" stroke-dasharray="58 193.3" transform="rotate(95)"/>
      <circle r="40" fill="none" stroke="var(--yellow)" stroke-width="13" stroke-dasharray="58 193.3" transform="rotate(185)"/>
      <circle r="40" fill="none" stroke="var(--orange)" stroke-width="13" stroke-dasharray="58 193.3" transform="rotate(275)"/>
    </g>
    <text x="150" y="96" text-anchor="middle" font-size="5" fill="#444">DESCRIPTION</text>
    <use href="#desc" x="22" y="66"/>
    <use href="#desc" x="22" y="122"/>
    <use href="#desc" x="208" y="50"/>
    <use href="#desc" x="208" y="108"/>
  </svg>

  <!-- Bar chart 3D -->
  <svg class="slide" style="left:924px;top:448px" viewBox="0 0 300 187">
    <rect width="300" height="187" fill="url(#slideBg)"/>
    <use href="#tab"/>
    <text class="title" x="19" y="25">Bar Chart</text>
    <polygon points="20,140 132,140 142,130 30,130" fill="#dfe8d4"/>
    <g class="stack">
      <rect x="35" y="90" width="18" height="12" fill="var(--purple)"/><rect x="35" y="102" width="18" height="12" fill="var(--yellow)"/><rect x="35" y="114" width="18" height="12" fill="var(--green-light)"/><rect x="35" y="126" width="18" height="12" fill="var(--orange)"/>
      <rect x="70" y="78" width="18" height="10" fill="var(--purple)"/><rect x="70" y="88" width="18" height="14" fill="var(--yellow)"/><rect x="70" y="102" width="18" height="24" fill="var(--green-light)"/><rect x="70" y="126" width="18" height="12" fill="var(--orange)"/>
      <rect x="107" y="82" width="18" height="16" fill="var(--purple)"/><rect x="107" y="98" width="18" height="12" fill="var(--yellow)"/><rect x="107" y="110" width="18" height="14" fill="var(--green-light)"/><rect x="107" y="124" width="18" height="14" fill="var(--orange)"/>
    </g>
    <g fill="#c8d0cc">
      <circle cx="44" cy="68" r="6"/><path d="M40 72l4 6 4-6z"/>
      <circle cx="80" cy="52" r="6"/><path d="M76 56l4 6 4-6z"/>
      <circle cx="117" cy="54" r="6"/><path d="M113 58l4 6 4-6z"/>
    </g>
    <g font-size="3.8" fill="#fff" text-anchor="middle"><text x="44" y="69.5">+70</text><text x="80" y="53.5">+80</text><text x="117" y="55.5">+60</text></g>
    <g text-anchor="middle"><text class="day" x="44" y="149">category 01</text><text class="day" x="80" y="152">category 02</text><text class="day" x="117" y="155">category 02</text></g>
    <use href="#desc" x="172" y="42"/>
    <use href="#desc" x="172" y="71"/>
    <use href="#desc" x="172" y="100"/>
    <use href="#desc" x="172" y="129"/>
  </svg>

  <!-- Bar chart grouped -->
  <svg class="slide" style="left:48px;top:630px" viewBox="0 0 300 187">
    <rect width="300" height="187" fill="url(#slideBg)"/>
    <use href="#tab"/>
    <text class="title" x="19" y="25">Bar Chart</text>
    <text class="heading" x="22" y="52">Super Plan 01</text>
    <use href="#bodyBlock" x="22" y="63"/>
    <use href="#bodyBlock" x="22" y="85"/>
    <use href="#legendList" x="22" y="123"/>
    <g class="bars">
      <rect x="140" y="88" width="8" height="62" fill="var(--yellow)"/><rect x="149" y="110" width="8" height="40" fill="var(--purple)"/><rect x="158" y="110" width="8" height="40" fill="var(--brown)"/><rect x="167" y="110" width="8" height="40" fill="var(--purple)"/>
      <rect x="188" y="110" width="8" height="40" fill="var(--yellow)"/><rect x="197" y="60" width="8" height="90" fill="var(--green-light)"/><rect x="206" y="110" width="8" height="40" fill="var(--brown)"/><rect x="215" y="110" width="8" height="40" fill="var(--purple)"/>
      <rect x="236" y="78" width="8" height="72" fill="var(--yellow)"/><rect x="245" y="112" width="8" height="38" fill="var(--green-light)"/><rect x="254" y="88" width="8" height="62" fill="var(--brown)"/><rect x="263" y="88" width="8" height="62" fill="var(--purple)"/>
    </g>
    <g fill="#c8d0cc">
      <circle cx="144" cy="72" r="6"/><path d="M140 76l4 6 4-6z"/>
      <circle cx="201" cy="44" r="6"/><path d="M197 48l4 6 4-6z"/>
      <circle cx="240" cy="62" r="6"/><path d="M236 66l4 6 4-6z"/>
    </g>
    <g font-size="3.8" fill="#fff" text-anchor="middle"><text x="144" y="73.5">+70</text><text x="201" y="45.5">+80</text><text x="240" y="63.5">+60</text></g>
    <g text-anchor="middle"><text class="day" x="158" y="156">category 01</text><text class="day" x="206" y="156">category 02</text><text class="day" x="254" y="156">category 02</text></g>
  </svg>

  <!-- Timeline horizontal -->
  <svg class="slide" style="left:318px;top:630px" viewBox="0 0 300 187">
    <rect width="300" height="187" fill="url(#slideBg)"/>
    <use href="#tab"/>
    <text class="title" x="19" y="25">Timeline</text>
    <line x1="15" y1="97" x2="285" y2="97" stroke="#c8d4d0" stroke-width="1.5"/>
    <g fill="#c8d4d0"><circle cx="65" cy="97" r="4"/><circle cx="122" cy="97" r="4"/><circle cx="178" cy="97" r="4"/><circle cx="235" cy="97" r="4"/></g>
    <g stroke="var(--green-light)" stroke-width="1"><line x1="40" y1="85" x2="90" y2="85"/><line x1="152" y1="85" x2="204" y2="85"/></g>
    <g text-anchor="middle">
      <text class="year" x="65" y="45">2013</text>
      <text class="body" x="65" y="53">Steady growth for root</text><text class="body" x="65" y="58">extracts across regions,</text><text class="body" x="65" y="63">with new partners</text><text class="body" x="65" y="68">joining this year.</text>
      <text class="year" x="178" y="45">2015</text>
      <text class="body" x="178" y="53">Steady growth for root</text><text class="body" x="178" y="58">extracts across regions,</text><text class="body" x="178" y="63">with new partners</text><text class="body" x="178" y="68">joining this year.</text>
      <text class="year" x="122" y="118">2014</text>
      <text class="body" x="122" y="126">New seed lines tested</text><text class="body" x="122" y="131">and approved for use</text><text class="body" x="122" y="136">in daily care ranges.</text>
      <text class="year" x="235" y="118">2016</text>
      <text class="body" x="235" y="126">New seed lines tested</text><text class="body" x="235" y="131">and approved for use</text><text class="body" x="235" y="136">in daily care ranges.</text>
    </g>
  </svg>

  <!-- Timeline with photos -->
  <svg class="slide" style="left:628px;top:630px" viewBox="0 0 300 187">
    <rect width="300" height="187" fill="url(#slideBg)"/>
    <use href="#tab"/>
    <text class="title" x="19" y="25">Timeline</text>
    <line x1="15" y1="97" x2="285" y2="97" stroke="#c8d4d0" stroke-width="1.5"/>
    <g fill="#c8d4d0"><circle cx="62" cy="97" r="4"/><circle cx="158" cy="97" r="4"/></g>
    <text class="year" x="55" y="46">2016</text>
    <rect x="35" y="50" width="54" height="36" fill="url(#phHarbour)" role="img" aria-label="Photo of a boat on the water"/>
    <use href="#desc" x="95" y="56"/>
    <rect x="131" y="112" width="54" height="36" fill="url(#phBlossom)" role="img" aria-label="Photo of pink blossoms"/>
    <text class="year" x="152" y="156">2015</text>
    <use href="#desc" x="190" y="116"/>
  </svg>

  <!-- Timeline vertical -->
  <svg class="slide" style="left:924px;top:630px" viewBox="0 0 300 187">
    <rect width="300" height="187" fill="url(#slideBg)"/>
    <g clip-path="url(#slideClip)">
      <circle cx="285" cy="80" r="105" fill="url(#phGold)" role="img" aria-label="Photo of a yellow flower"/>
    </g>
    <circle cx="228" cy="148" r="36" fill="url(#phRoot)" stroke="#fff" stroke-width="2" role="img" aria-label="Photo of dried herb"/>
    <use href="#tab"/>
    <text class="title" x="19" y="25">Timeline</text>
    <line x1="53" y1="42" x2="53" y2="160" stroke="#c8d4d0" stroke-width="1"/>
    <g text-anchor="end"><text class="tl-year" x="48" y="50">2012</text><text class="tl-year" x="48" y="76">2013</text><text class="tl-year" x="48" y="102">2014</text><text class="tl-year" x="48" y="128">2015</text><text class="tl-year" x="48" y="154">2016</text></g>
    <g fill="#c8d4d0"><circle cx="53" cy="48" r="2"/><circle cx="53" cy="74" r="2"/><circle cx="53" cy="100" r="2"/><circle cx="53" cy="126" r="2"/><circle cx="53" cy="152" r="2"/></g>
    <use href="#desc" x="60" y="44"/><use href="#desc" x="60" y="70"/><use href="#desc" x="60" y="96"/><use href="#desc" x="60" y="122"/><use href="#desc" x="60" y="148"/>
  </svg>

  <!-- World map 1 -->
  <svg class="slide" style="left:48px;top:818px" viewBox="0 0 300 187">
    <rect width="300" height="187" fill="url(#slideBg)"/>
    <use href="#tab"/>
    <text class="title" x="19" y="25">Vector World Map</text>
    <rect x="40" y="35" width="240" height="105" rx="18" fill="#dcdedc" opacity=".8" role="img" aria-label="World map with highlighted regions in purple, yellow, green and orange"/>
    <g fill="#fff" stroke="#e6e6e6" stroke-width=".5">
      <rect x="16" y="48" width="70" height="32"/><rect x="208" y="40" width="76" height="30"/><rect x="96" y="98" width="50" height="22"/><rect x="158" y="76" width="46" height="22"/>
    </g>
    <use href="#desc" x="22" y="55"/><use href="#desc" x="214" y="47"/><use href="#desc" x="101" y="105"/><use href="#desc" x="162" y="83"/>
    <use href="#legendList" x="16" y="150"/>
  </svg>

  <!-- World map 2 -->
  <svg class="slide" style="left:318px;top:818px" viewBox="0 0 300 187">
    <rect width="300" height="187" fill="url(#slideBg)"/>
    <use href="#tab"/>
    <text class="title" x="19" y="25">Vector World Map</text>
    <rect x="30" y="38" width="230" height="100" rx="18" fill="#d8dad8" opacity=".8" role="img" aria-label="World map in grey"/>
    <g class="pins">
      <circle cx="66" cy="66" r="7" fill="var(--purple)"/><path d="M60 69l6 10 6-10z" fill="var(--purple)"/>
      <circle cx="111" cy="42" r="7" fill="var(--yellow)"/><path d="M105 45l6 10 6-10z" fill="var(--yellow)"/>
      <circle cx="196" cy="55" r="7" fill="var(--green-light)"/><path d="M190 58l6 10 6-10z" fill="var(--green-light)"/>
      <circle cx="147" cy="97" r="7" fill="var(--brown)"/><path d="M141 100l6 10 6-10z" fill="var(--brown)"/>
    </g>
    <use href="#legendList" x="16" y="150"/>
  </svg>

  <!-- Thank you -->
  <svg class="slide" style="left:628px;top:818px" viewBox="0 0 300 187">
    <rect width="300" height="187" fill="url(#slideBg)"/>
    <text x="27" y="47" font-size="19" font-weight="300" fill="var(--purple)">Thanks you so much!</text>
    <line x1="27" y1="57" x2="300" y2="57" stroke="#dfe6d6" stroke-width=".6"/>
    <text x="27" y="71" font-size="5" fill="#b0b0b0">For more info please contact us</text>
    <text x="27" y="90" font-size="7" fill="#444">012-345-6789-100</text>
    <text x="27" y="101" font-size="7" fill="#444">lena.marovic@herbalstudio.example</text>
    <text x="27" y="123" font-size="4.5" fill="#444"><tspan font-weight="700">Lena Marovic</tspan>/ Feb 29, 2016</text>
    <rect y="140" width="300" height="47" fill="url(#phLavender)" role="img" aria-label="Photo of purple lavender flowers"/>
  </svg>

</main>
</body>
</html>
```